Request for Business Card Design

Hi. My name is Marlena, I am looking for a new business card design for my company, Quillbrook Sensing Systems, LLC. I really like the design you did for Tavel Harvest and was hoping you could do something similar using our full logo and our mark. I am also open to any raised texture design using our mark. I have attached our full logo, which would need to be somewhere on the card, as well as the mark in both outline and full form, as well as our brand colors / guide. The card does not have to be white, as long as our logo and mark appear. I actually like darker colored business cards more, but am open to all options. If you are interested in working with me, please let me know. We would also take the business card design into letterhead design if you can do that.

```html
<!DOCTYPE html>
<html lang="en">
<head>
<meta charset="utf-8">
<title>Quillbrook Sensing Systems — Business Card</title>
<link rel="stylesheet" href="https://fonts.googleapis.com/css2?family=Montserrat:wght@400;500;700;800&display=swap">
<style>
  :root {
    --backdrop: #141414;
    --card-top: #333333;
    --card-bottom: #474747;
    --brand-blue: #1c9fd0;
    --emboss-text: #2c2c2c;
    --faint-mark: #44575d;
    --ink-light: #ffffff;
  }
  * { margin: 0; padding: 0; box-sizing: border-box; }
  html, body {
    width: 1200px; height: 900px; overflow: hidden;
    background: var(--backdrop);
    font-family: "Montserrat", sans-serif;
  }
  .canvas { position: relative; width: 1200px; height: 900px; }
  .card {
    position: absolute; left: 280px; width: 640px; height: 366px;
    background: linear-gradient(160deg, var(--card-top), var(--card-bottom));
    overflow: hidden;
  }
  .card--back { top: 42px; }
  .card--front { top: 470px; }

  /* back: embossed wordmark */
  .emboss {
    position: absolute; left: 0; right: 0; top: 140px; text-align: center;
    color: var(--emboss-text);
  }
  .emboss__name {
    font-weight: 800; font-size: 50px; letter-spacing: 5px; line-height: 1;
  }
  .emboss__tagline {
    margin-top: 8px; font-weight: 700; font-size: 13px; letter-spacing: 2px;
  }

  /* front */
  .faint-mark {
    position: absolute; right: -150px; top: 60px;
    width: 420px; height: 420px; border-radius: 50%;
    background: var(--faint-mark); opacity: 0.75;
  }
  .brand { position: absolute; left: 44px; top: 36px; display: flex; align-items: center; gap: 16px; }
  .brand__dot { width: 44px; height: 44px; border-radius: 50%; background: var(--brand-blue); }
  .brand__name { color: var(--ink-light); font-weight: 800; font-size: 30px; letter-spacing: 4px; line-height: 1; }
  .brand__tagline { color: var(--ink-light); font-weight: 700; font-size: 9.5px; letter-spacing: 1.2px; margin-top: 5px; }

  .person { position: absolute; left: 0; top: 122px; padding-left: 40px; }
  .person__bar { position: absolute; left: 0; top: 2px; width: 20px; height: 48px; background: var(--brand-blue); }
  .person__name { color: var(--brand-blue); font-weight: 800; font-size: 26px; letter-spacing: 1.5px; line-height: 1.05; }
  .person__role { color: var(--ink-light); font-weight: 500; font-size: 13px; letter-spacing: 1px; }

  .address { position: absolute; left: 40px; top: 196px; color: var(--ink-light); font-size: 13px; line-height: 1.45; }
  .contacts { position: absolute; left: 40px; top: 248px; list-style: none; color: var(--ink-light); font-size: 13px; }
  .contacts li { display: flex; align-items: center; gap: 10px; height: 22px; }
  .contacts svg { width: 13px; height: 13px; fill: var(--brand-blue); flex: none; }
</style>
</head>
<body>
<main class="canvas">
  <section class="card card--back" aria-label="Card back">
    <div class="emboss">
      <div class="emboss__name">QUILLBROOK</div>
      <div class="emboss__tagline">SENSING SYSTEMS</div>
    </div>
  </section>

  <section class="card card--front" aria-label="Card front">
    <div class="faint-mark"></div>
    <div class="brand">
      <div class="brand__dot"></div>
      <div>
        <div class="brand__name">QUILLBROOK</div>
        <div class="brand__tagline">SENSING SYSTEMS</div>
      </div>
    </div>

    <div class="person">
      <div class="person__bar"></div>
      <div class="person__name">TOBIN ASHGROVE</div>
      <div class="person__role">MANAGER</div>
    </div>

    <p class="address">482 Linden Hollow Road 12<br>Fairmere, MN 55021</p>

    <ul class="contacts">
      <li>
        <svg viewBox="0 0 16 16"><path d="M3.5 1l2.5 3-1.5 1.8c.9 2 2.6 3.7 4.7 4.7L11 9l3 2.5-1.3 2.8C7 14 2 9 1.7 3.3z"/></svg>
        (555)210-4471
      </li>
      <li>
        <svg viewBox="0 0 16 16"><path d="M4.5 0h7A1.5 1.5 0 0 1 13 1.5v13a1.5 1.5 0 0 1-1.5 1.5h-7A1.5 1.5 0 0 1 3 14.5v-13A1.5 1.5 0 0 1 4.5 0zM5 2v10h6V2zm3 11a1 1 0 1 0 0 2 1 1 0 0 0 0-2z"/></svg>
        (555)318-90210
      </li>
      <li>
        <svg viewBox="0 0 16 16"><path d="M1 3h14v1.2L8 8.8 1 4.2zM1 5.6l7 4.6 7-4.6V13H1z"/></svg>
        info@quillbrook.com
      </li>
      <li>
        <svg viewBox="0 0 16 16"><path d="M8 0a8 8 0 1 0 0 16A8 8 0 0 0 8 0zm5.9 7h-2.6a12 12 0 0 0-1-4.8A6 6 0 0 1 13.9 7zM8 2c.7 1 1.2 2.8 1.3 5H6.7C6.8 4.8 7.3 3 8 2zM5.7 2.2a12 12 0 0 0-1 4.8H2.1a6 6 0 0 1 3.6-4.8zM2.1 9h2.6a12 12 0 0 0 1 4.8A6 6 0 0 1 2.1 9zM8 14c-.7-1-1.2-2.8-1.3-5h2.6c-.1 2.2-.6 4-1.3 5zm2.3-.2a12 12 0 0 0 1-4.8h2.6a6 6 0 0 1-3.6 4.8z"/></svg>
        www.quillbrooksensing.com
      </li>
    </ul>
  </section>
</main>
</body>
</html>
```